VENTURE CAPITAL GROUP BUSINESS CARD DESIGN

Venture Capital Group based in SF looking for a bold business card design. No trendy colour explosion, 3D effects etc. Just "simple" optical effects. Works on your brain, keeps your eye focused and sticks to your mind.
Target Market(s)
Technology startups
Industry/Entity Type
Venture Capital
Contact Information for Business Card
BARTHOLOMEW ELLING
MANAGING PARTNER
817 FERN ST SAN FRANCISCO, CA 94111
415.555.0142 O
415.555.0187 F
415.555.0236 C
bart@quillbrookfunds.example

```html
<!DOCTYPE html>
<html lang="en">
<head>
<meta charset="utf-8">
<title>Quillbrook Capital Group — Business Card</title>
<link href="https://fonts.googleapis.com/css2?family=Cinzel:wght@400&family=Roboto:wght@400;700&display=swap" rel="stylesheet">
<style>
  :root {
    --backdrop: #3a3a3c;
    --green-deep: #1f7a2e;
    --green-mid: #3a9a40;
    --green-light: #5cb85a;
    --brand-green: #1d8a34;
    --card-white: #fbfbfb;
    --ink: #2b2b2b;
    --muted: #8a8a8a;
  }
  * { margin: 0; padding: 0; box-sizing: border-box; }
  html, body { width: 1200px; height: 1019px; overflow: hidden; }
  body { background: var(--backdrop); position: relative; font-family: "Roboto", Arial, sans-serif; }

  .card {
    position: absolute;
    width: 630px;
    height: 360px;
    overflow: hidden;
    box-shadow: 0 10px 30px rgba(0,0,0,.45);
  }

  /* Front */
  .card-front {
    left: 110px; top: 100px;
    background: radial-gradient(ellipse at 62% 38%, var(--green-light) 0%, var(--green-mid) 45%, var(--green-deep) 100%);
    display: flex; flex-direction: column; align-items: center; justify-content: center;
  }
  .front-wordmark {
    font-family: "Cinzel", Georgia, serif;
    color: #fff;
    text-align: center;
    font-weight: 400;
  }
  .front-wordmark .name { display: block; font-size: 46px; letter-spacing: 2px; line-height: 1; }
  .front-wordmark .sub { display: block; font-size: 13px; letter-spacing: 6px; margin-top: 8px; }

  /* Back */
  .card-back {
    left: 460px; top: 560px;
    background: var(--card-white);
  }
  .edge-tab {
    position: absolute; right: 0; top: 52px;
    width: 12px; height: 30px; background: var(--brand-green);
  }
  .holder {
    position: absolute; right: 30px; top: 50px; text-align: right;
  }
  .holder-name { color: var(--brand-green); font-weight: 700; font-size: 17px; letter-spacing: .3px; }
  .holder-title { color: var(--muted); font-size: 13px; letter-spacing: .3px; margin-top: 2px; }

  .back-wordmark {
    position: absolute; left: 40px; top: 150px;
    font-family: "Cinzel", Georgia, serif;
    color: var(--brand-green); font-weight: 400;
  }
  .back-wordmark .name { display: block; font-size: 28px; letter-spacing: 1px; line-height: 1; }
  .back-wordmark .sub { display: block; font-size: 9px; letter-spacing: 4px; margin-top: 5px; }

  .contact {
    position: absolute; left: 40px; top: 222px;
    list-style: none; color: var(--ink); font-size: 14px; line-height: 22px;
  }
  .contact li { display: flex; align-items: center; gap: 8px; }
  .contact .address { margin-bottom: 2px; }
  .contact svg { width: 13px; height: 13px; flex: none; fill: var(--brand-green); }
</style>
</head>
<body>

  <section class="card card-front" aria-label="Card front">
    <div class="front-wordmark">
      <span class="name">QUILLBROOK</span>
      <span class="sub">CAPITAL GROUP</span>
    </div>
  </section>

  <section class="card card-back" aria-label="Card back">
    <div class="edge-tab"></div>
    <div class="holder">
      <div class="holder-name">BARTHOLOMEW ELLING</div>
      <div class="holder-title">MANAGING PARTNER</div>
    </div>

    <div class="back-wordmark">
      <span class="name">QUILLBROOK</span>
      <span class="sub">CAPITAL GROUP</span>
    </div>

    <ul class="contact">
      <li class="address">817 FERN ST SAN FRANCISCO, CA 94111</li>
      <li>
        <svg viewBox="0 0 16 16"><path d="M3 1l3 3-2 2c1 2 3 4 5 5l2-2 3 3-2 3C6 14 2 10 1 3z"/></svg>
        415.555.0142
      </li>
      <li>
        <svg viewBox="0 0 16 16"><rect x="4" y="1" width="8" height="4"/><rect x="1" y="6" width="14" height="6" rx="1"/><rect x="4" y="10" width="8" height="5"/></svg>
        415.555.0187
      </li>
      <li>
        <svg viewBox="0 0 16 16"><path d="M4 1h8v14H4z M5.5 2.5v9h5v-9z" fill-rule="evenodd"/></svg>
        415.555.0236
      </li>
      <li>
        <svg viewBox="0 0 16 16"><path d="M1 3h14v10H1z M2.5 4.5L8 9l5.5-4.5" fill-rule="evenodd"/></svg>
        bart@quillbrookfunds.example
      </li>
    </ul>
  </section>

</body>
</html>
```